It is a leisure sector investment company.The company plans to invest in a luxurious 5 star resort

We need a stationery design to our company 'Copper Lantern Limited' using the winning logo design. We need the letter heads, envelopes & the business cards. Should be simple, plain and professional
We have upload the source file & vector files which gives our logo design. We prefer the bottom logo.

Have updated under 'must have priorities', the company name, address, tel no. fax no. & the company reg no. which should come on the letter head. the long envelope should have the company name, tel & fax no. 
Business card should have the company name, name on the card, designation, tel no. fax no.  

- Letter head details:
Copper Lantern Limited
14 Floor, South Wing, Halvard Merchant Plaza,
Merrow Court, Colombo 01, Sri Lanka
Tel: +94 11 5047293 Fax: +94 11 5047298
Company Reg No.QX 6142
Long Envelope should have only the company name, adress, Tel & Fax
Business Cards should have the company name, Tel & Fax:
Business Card 1 - Lasantha Gunaratne - Chairman
Business Card 2 - Nimal.T.Wijesooriya - COO

```html
<!DOCTYPE html>
<html lang="en">
<head>
<meta charset="utf-8">
<title>Copper Lantern Limited – Business Cards</title>
<link rel="stylesheet" href="https://fonts.googleapis.com/css2?family=Tinos:wght@400;700&family=Arimo:wght@400&display=swap">
<style>
  :root {
    --page: #ffffff;
    --label: #111111;
    --card-brown: #5b4a41;
    --card-brown-edge: #4a3b33;
    --ornament-dark: #2a201b;
    --card-white: #ffffff;
    --card-border: #9a9a9a;
    --ink-brown: #5b4a41;
    --ink-dark: #2b2522;
    --rule: #4b3e37;
  }
  * { box-sizing: border-box; margin: 0; padding: 0; }
  html, body { width: 1200px; height: 900px; overflow: hidden; background: var(--page); }
  .sheet { position: relative; width: 1200px; height: 900px; font-family: "Tinos", "Times New Roman", serif; }

  .set-label {
    position: absolute; left: 120px;
    font-family: "Arimo", Arial, sans-serif; font-size: 22px; color: var(--label);
  }

  .card { position: absolute; width: 426px; height: 252px; border-radius: 12px; overflow: hidden; }

  .card-front { background: var(--card-brown); left: 216px; }
  .card-front .front-bottom-rule {
    position: absolute; left: 0; right: 0; bottom: 10px; height: 3px; background: var(--ornament-dark);
  }
  .front-crest {
    position: absolute; left: 154px; top: 48px; width: 140px; height: 42px; border-radius: 6px;
    background: radial-gradient(ellipse at center, var(--ornament-dark) 40%, var(--card-brown) 100%);
  }
  .front-name {
    position: absolute; left: 0; right: 0; top: 96px; text-align: center;
    font-size: 36px; letter-spacing: 1px; color: var(--ornament-dark); line-height: 1.05;
  }
  .front-name small { display: block; font-size: 20px; letter-spacing: 6px; }
  .front-flourish {
    position: absolute; right: 0; bottom: 0; width: 140px; height: 72px;
    background: linear-gradient(135deg, var(--card-brown) 10%, var(--ornament-dark) 85%);
    border-top-left-radius: 70px 60px;
  }

  .card-back { background: var(--card-white); border: 2px solid var(--card-border); left: 646px; }
  .back-flourish {
    position: absolute; left: 0; bottom: 0; width: 114px; height: 72px;
    background: linear-gradient(225deg, var(--card-white) 10%, var(--ornament-dark) 90%);
    border-top-right-radius: 80px 60px; opacity: 0.9;
  }
  .holder { position: absolute; left: 38px; top: 54px; font-size: 18px; color: var(--ink-brown); }
  .contact { position: absolute; left: 86px; top: 88px; font-size: 14px; line-height: 22px; color: var(--ink-dark); }
  .contact .company { color: var(--ink-brown); }
  .divider { position: absolute; left: 258px; top: 72px; width: 2px; height: 140px; background: var(--rule); }
  .back-mark {
    position: absolute; left: 296px; top: 168px; width: 110px; text-align: center;
    font-size: 11px; line-height: 13px; color: var(--ink-brown);
  }
  .back-rule { position: absolute; left: 92px; right: 0; top: 226px; height: 2px; background: var(--rule); }
</style>
</head>
<body>
<main class="sheet">

  <p class="set-label" style="top:82px">Business Card 1</p>
  <section class="card card-front" style="top:136px" aria-label="Card front">
    <div class="front-crest" role="img" aria-label="Decorative crest ornament"></div>
    <p class="front-name">COPPER LANTERN<small>LIMITED</small></p>
    <div class="front-flourish" role="img" aria-label="Decorative floral flourish"></div>
    <div class="front-bottom-rule"></div>
  </section>
  <section class="card card-back" style="top:136px" aria-label="Card back">
    <p class="holder">Lasantha Gunaratne - Chairman</p>
    <div class="contact">
      <p class="company">Copper Lantern Limited</p>
      <p>Tel: +94 11 5047293</p>
      <p>Fax: +94 11 5047298</p>
    </div>
    <div class="divider"></div>
    <p class="back-mark">COPPER LANTERN LIMITED</p>
    <div class="back-rule"></div>
    <div class="back-flourish" role="img" aria-label="Decorative floral flourish"></div>
  </section>

  <p class="set-label" style="top:494px">Business Card 2</p>
  <section class="card card-front" style="top:544px" aria-label="Card front">
    <div class="front-crest" role="img" aria-label="Decorative crest ornament"></div>
    <p class="front-name">COPPER LANTERN<small>LIMITED</small></p>
    <div class="front-flourish" role="img" aria-label="Decorative floral flourish"></div>
    <div class="front-bottom-rule"></div>
  </section>
  <section class="card card-back" style="top:544px" aria-label="Card back">
    <p class="holder">Nimal.T.Wijesooriya - COO</p>
    <div class="contact">
      <p class="company">Copper Lantern Limited</p>
      <p>Tel: +94 11 5047293</p>
      <p>Fax: +94 11 5047298</p>
    </div>
    <div class="divider"></div>
    <p class="back-mark">COPPER LANTERN LIMITED</p>
    <div class="back-rule"></div>
    <div class="back-flourish" role="img" aria-label="Decorative floral flourish"></div>
  </section>

</main>
</body>
</html>
```